Modern Business Card Design for Independent Urban Music Label

We need a card design for an independent urban music label called Copper Kite Records based in London. We develop and promote urban British music artists. We attend lots of high profile events with high profile industry people and want a card that comes across both on-brand and sophisticated, professional, trustworthy. I have attached our logo - please use the black and orange version in the upper left HOWEVER we are open to seeing other colors than the orange used though we want the shape of the logo to remain the same.

Info to please include:
Name
Position
Phone
Email
Website

Additional Info:
Twitter: @CopperKiteRecsUK
Insta: @CopperKiteRecs

Target Market(s)

Industry professionals and others artists

Industry/Entity Type

Business

Contact Information for Business Card

Info to please include:
Name
Position
Phone
Email
Website

Additional Info:
Twitter: @CopperKiteRecsUK
Insta: @CopperKiteRecs

Requirements
Must have
• Logo, company name
• Info to please include:
• Name
• Position
• Phone
• Email
• Website
Nice to have
• Twitter: @CopperKiteRecsUK
• Insta: @CopperKiteRecs
• If it can be done so that it doesn't look cluttered

```html
<!DOCTYPE html>
<html lang="en">
<head>
<meta charset="utf-8">
<title>Copper Kite Records — Business Card</title>
<link href="https://fonts.googleapis.com/css2?family=Bebas+Neue&display=swap" rel="stylesheet">
<style>
  :root {
    --paper: #ffffff;
    --ink: #111111;
    --copper: #f47b4b;
    --bleed-line: #e02424;
    --trim-line: #2ee6f0;
  }
  * { box-sizing: border-box; margin: 0; padding: 0; }
  html, body {
    width: 1200px;
    height: 702px;
    overflow: hidden;
    background: var(--paper);
  }
  .card {
    position: relative;
    width: 1200px;
    height: 702px;
    background: var(--paper);
    font-family: "Bebas Neue", "Oswald", sans-serif;
  }
  .bleed-frame {
    position: absolute;
    left: 22px; top: 20px;
    width: 1156px; height: 664px;
    border: 3px solid var(--bleed-line);
  }
  .trim-frame {
    position: absolute;
    left: 45px; top: 45px;
    width: 1113px; height: 617px;
    border: 3px solid var(--trim-line);
  }
  .brand {
    position: absolute;
    left: 0; right: 0;
    top: 250px;
    display: flex;
    align-items: center;
    justify-content: center;
    gap: 22px;
  }
  .brand-dot {
    width: 58px; height: 58px;
    border-radius: 50%;
    background: var(--ink);
    flex: none;
  }
  .brand-name {
    color: var(--copper);
    font-size: 66px;
    line-height: 1;
    letter-spacing: 3px;
    text-transform: uppercase;
    font-weight: 400;
  }
  .socials {
    position: absolute;
    left: 0; right: 0;
    top: 556px;
    display: flex;
    justify-content: center;
    gap: 38px;
  }
  .social {
    display: flex;
    align-items: center;
    gap: 12px;
    color: var(--copper);
    font-size: 32px;
    line-height: 1;
    letter-spacing: 0.5px;
    text-transform: uppercase;
  }
  .social-mark {
    width: 24px; height: 24px;
    background: var(--copper);
    flex: none;
  }
  .social-mark--round { border-radius: 50%; }
</style>
</head>
<body>
  <main class="card">
    <div class="bleed-frame" aria-hidden="true"></div>
    <div class="trim-frame" aria-hidden="true"></div>

    <div class="brand">
      <span class="brand-dot" aria-hidden="true"></span>
      <h1 class="brand-name">Copper Kite Records</h1>
    </div>

    <ul class="socials" style="list-style:none">
      <li class="social">
        <span class="social-mark social-mark--round" aria-hidden="true"></span>
        <span class="social-handle">@CopperKiteRecsUK</span>
      </li>
      <li class="social">
        <span class="social-mark" aria-hidden="true"></span>
        <span class="social-handle">@CopperKiteRecsUK</span>
      </li>
    </ul>
  </main>
</body>
</html>
```